PLATRIX passionate and energetic Business Card

We need a business card design for a new company based in Melbourne called "PLATRIX" www.platrix.com.au. We delivery food to the customer, we got 80+ restaurant at the moment. We would like to see designs that use the color red pearl white. The final design should be looks passionate and energetic. Should be related to the website www.platrix.com.au

Target Market(s)

18-55 AGE

Industry/Entity Type

Business

Contact Information for Business Card

Fast Easy way to get food order on the internet.

Font styles to use
Serif
Sans Serif
Decorative

Colors
ec1f27
fff5ef

Requirements
Must have
• Should relative to the website www.platrix.com.au
Nice to have
• No Idea
Should not have
• No Idea

```html
<!DOCTYPE html>
<html lang="en">
<head>
<meta charset="utf-8">
<title>PLATRIX Business Card</title>
<link rel="stylesheet" href="https://fonts.googleapis.com/css2?family=Noto+Sans:wght@400;700&family=Noto+Sans+SC:wght@400&family=Playfair+Display:ital@1&display=swap">
<style>
  :root {
    --page-bg: #e8e5e2;
    --card-face: #f3efec;
    --panel-black: #0b0b0c;
    --brand-red: #ec1f27;
    --deep-red: #b5121b;
    --ink: #1c1c1c;
    --pearl: #fff5ef;
  }
  html, body {
    margin: 0;
    width: 1200px;
    height: 970px;
    overflow: hidden;
    background: var(--page-bg);
  }
  .card {
    position: absolute;
    left: 120px;
    top: 218px;
    width: 960px;
    height: 533px;
    background: linear-gradient(135deg, var(--pearl) 0%, var(--card-face) 60%, #e9e3de 100%);
    overflow: hidden;
    box-shadow: 0 10px 30px rgba(0,0,0,0.18);
    font-family: "Noto Sans", Arial, sans-serif;
    color: var(--ink);
  }
  .card__panel {
    position: absolute;
    left: 0;
    top: 0;
    width: 420px;
    height: 533px;
  }
  .brand-name {
    position: absolute;
    left: 178px;
    top: 266px;
    transform: translate(-50%, -50%) rotate(-90deg);
    font-family: "Noto Sans", Arial, sans-serif;
    font-weight: 700;
    font-size: 90px;
    line-height: 1;
    letter-spacing: 3px;
    color: var(--brand-red);
    white-space: nowrap;
  }
  .slogan {
    position: absolute;
    left: 118px;
    top: 208px;
    transform: translate(-50%, -50%) rotate(-90deg);
    font-family: "Noto Sans SC", "Noto Sans", sans-serif;
    font-size: 22px;
    line-height: 1;
    letter-spacing: 1px;
    color: var(--pearl);
    white-space: nowrap;
  }
  .produce-photo {
    position: absolute;
    right: 0;
    top: 0;
    width: 144px;
    height: 163px;
    background: linear-gradient(200deg, #c9201a 0%, #e0524a 55%, #f1ddd6 100%);
  }
  .person-name {
    position: absolute;
    left: 458px;
    top: 80px;
    font-family: "Playfair Display", Georgia, serif;
    font-style: italic;
    font-size: 36px;
    color: var(--ink);
  }
  .person-title {
    position: absolute;
    left: 460px;
    top: 137px;
    font-size: 19px;
  }
  .address {
    position: absolute;
    left: 458px;
    top: 296px;
    font-size: 21px;
  }
  .contact-list {
    position: absolute;
    left: 458px;
    top: 350px;
    margin: 0;
    padding: 0;
    list-style: none;
    font-size: 21px;
  }
  .contact-list li {
    display: flex;
    align-items: center;
    height: 32px;
  }
  .contact-list svg {
    width: 22px;
    height: 18px;
    margin-right: 20px;
    fill: var(--brand-red);
  }
</style>
</head>
<body>
  <div class="card">
    <svg class="card__panel" viewBox="0 0 420 533" aria-hidden="true">
      <path d="M0 0 H368 C348 120 398 230 388 330 C378 430 348 480 338 533 H0 Z" fill="var(--deep-red)"/>
      <path d="M0 0 H352 C332 120 382 230 372 330 C362 430 332 480 322 533 H0 Z" fill="var(--panel-black)"/>
    </svg>
    <div class="slogan">保温配送 风雨无阻</div>
    <div class="brand-name">PLATRIX</div>

    <div class="produce-photo" role="img" aria-label="Photo of fresh red cherry tomatoes"></div>

    <div class="person-name">Your Name</div>
    <div class="person-title">Title</div>

    <div class="address">1507/88 Harbour Rd, Melbourne, 3000.</div>
    <ul class="contact-list">
      <li>
        <svg viewBox="0 0 24 20"><path d="M3 6 C3 3 6 2 12 2 C18 2 21 3 21 6 L17 7 L16 5 H8 L7 7 Z M6 8 H18 L20 18 H4 Z"/></svg>
        03 9100 2468, 0400 135 792
      </li>
      <li>
        <svg viewBox="0 0 24 18"><path d="M1 2 H23 V16 H1 Z M3 4 V14 H21 V4 L12 10 Z" fill-rule="evenodd"/></svg>
        admin@platrix.com.au
      </li>
      <li>
        <svg viewBox="0 0 20 20"><circle cx="10" cy="10" r="9"/><path d="M1 10 H19 M10 1 V19 M3 5 H17 M3 15 H17" stroke="#fff" stroke-width="1.2" fill="none"/></svg>
        www.platrix.com.au
      </li>
    </ul>
  </div>
</body>
</html>
```